Back to School Fair Sponsor Opportunities

We mainly need the cover designed and a continuation of design throughout. The other three pages are basically done just need to be inserted.

Cover will include our Logo, Back to School Fair title at top, photo in center, and date/time at bottom. Please also include "Sponsor Opportunities" or a phrase similar at the bottom.

2 page brochure that's 11x17 full color folded in half (so there are four 8.5x11 panels) with the order form on the back.

Target Market(s)

Corporations

Industry/Entity Type

School

Font styles to use
Serif

Requirements
Must have
• All files must be included with the specifications outlined above.
• Colors that compliment our logo color.
• Please pull detailed information from the files included. (i.e. time/date)
• Order form on the back.
Nice to have
• Please remove the yellow background color to the image if you would like to use a different background.
• Incorporate a few of the event photos into the inside page 2 to break up some of the text.

```html
<!DOCTYPE html>
<html lang="en">
<head>
<meta charset="utf-8">
<title>Back to School Fair – Sponsor Opportunities</title>
<link rel="stylesheet" href="https://fonts.googleapis.com/css2?family=Playfair+Display:ital,wght@0,400;0,700;1,400&family=Open+Sans:wght@400;600;700&display=swap">
<style>
:root{
  --pink:#e0457b;
  --pink-soft:#f7c6d7;
  --pink-pale:#fdeef3;
  --ink:#4a4a4a;
  --muted:#8a8a8a;
  --paper:#ffffff;
  --ground:#ececec;
  --photo-warm:#e9c6a8;
  --photo-cool:#c9d8e6;
}
*{box-sizing:border-box;margin:0;padding:0}
html,body{width:865px;height:1200px;overflow:hidden;background:var(--ground)}
body{font-family:"Open Sans",Arial,sans-serif;color:var(--ink);position:relative}
.spread{position:absolute;left:32px;width:800px;height:518px;display:flex;background:var(--paper)}
.spread--outside{top:36px}
.spread--inside{top:626px}
.panel{position:relative;width:400px;height:518px;overflow:hidden;background:var(--paper)}
.panel + .panel{border-left:1px solid #eee}
.photo{position:absolute}
.brand{font-family:"Playfair Display",Georgia,serif;font-weight:700;color:var(--pink);line-height:1;display:flex;align-items:center;gap:6px;white-space:nowrap}
.brand i{display:inline-block;width:9px;height:9px;border-radius:50%;background:var(--pink);flex:none}
.serif{font-family:"Playfair Display",Georgia,serif}
.small{font-size:6.5px;line-height:1.45}

/* order form panel */
.order__photo{left:0;top:0;width:400px;height:120px;background:linear-gradient(120deg,var(--photo-cool),var(--photo-warm))}
.order__brand{position:absolute;left:24px;top:132px;font-size:22px}
.form-lines{position:absolute;left:24px;top:170px;width:352px}
.form-lines div{display:flex;align-items:flex-end;gap:6px;font-size:6.5px;font-weight:600;text-transform:uppercase;height:15px}
.form-lines span.line{flex:1;border-bottom:1px solid #bbb}
.levels{position:absolute;left:24px;top:262px;width:352px;border-collapse:collapse;font-size:6.5px}
.levels td{padding:5px 4px;border-bottom:1px solid #e3e3e3}
.levels td:last-child{text-align:right;color:var(--pink);font-weight:700}
.order__sign{position:absolute;left:24px;top:420px;width:352px;font-size:6.5px}
.order__sign div{border-bottom:1px solid #bbb;height:16px;display:flex;align-items:flex-end}
.order__band{position:absolute;left:0;bottom:0;width:400px;height:26px;background:var(--pink)}

/* cover panel */
.cover__photo{left:0;top:0;width:400px;height:300px;background:radial-gradient(circle at 60% 50%,var(--photo-warm),#f4e3d6 60%,var(--paper))}
.cover__curve{position:absolute;left:0;top:250px}
.badge{position:absolute;left:302px;top:86px;width:76px;height:76px;border-radius:50%;background:var(--pink);color:#fff;display:flex;align-items:center;justify-content:center;text-align:center;font-size:8px;font-weight:700;text-transform:uppercase;line-height:1.25;padding:8px}
.cover__title{position:absolute;right:22px;top:316px;width:350px;text-align:right;color:var(--pink);font-size:15px;line-height:1.2;text-transform:uppercase}
.cover__lede{position:absolute;right:22px;top:364px;width:230px;text-align:right;font-family:"Playfair Display",Georgia,serif;font-style:italic;font-size:10px;line-height:1.35}
.cover__brand{position:absolute;right:22px;bottom:34px;font-size:30px}
.cover__brand-wrap{position:absolute;right:22px;bottom:70px;font-size:7px;letter-spacing:2px;color:var(--muted);text-transform:uppercase}

/* inside left */
.intro__brand{position:absolute;left:24px;top:24px;font-size:19px}
.intro__text{position:absolute;left:24px;top:60px;width:170px}
.intro__photo{left:206px;top:22px;width:170px;height:170px;background:linear-gradient(150deg,var(--photo-warm),var(--photo-cool))}
.datebox{position:absolute;left:24px;top:205px;width:170px;background:var(--pink);color:#fff;padding:10px;font-size:7.5px;line-height:1.45;font-weight:600}
.h-pink{color:var(--pink);font-family:"Playfair Display",Georgia,serif;font-weight:700;font-size:11px;margin:0 0 4px}
.who{position:absolute;left:24px;top:282px;width:170px}
.why{position:absolute;left:206px;top:205px;width:170px}
.intro__band{position:absolute;left:0;bottom:0;width:400px;height:54px;background:var(--pink);color:#fff;text-align:center;font-size:8px;font-weight:600;line-height:1.5;padding-top:14px}
.intro__curve{position:absolute;left:0;bottom:48px}

/* inside right */
.tiers__photo{left:0;top:0;width:400px;height:128px;background:linear-gradient(100deg,var(--photo-cool),var(--photo-warm) 70%)}
.tier{position:absolute;width:170px}
.tier ul{list-style:none}
.tier li{position:relative;padding-left:8px}
.tier li::before{content:"";position:absolute;left:0;top:3px;width:4px;height:4px;border-radius:50%;background:var(--pink)}
.tiers__inset{left:24px;top:338px;width:170px;height:110px;background:linear-gradient(160deg,var(--photo-warm),var(--pink-soft))}
.tiers__curve{position:absolute;left:0;bottom:0}
</style>
</head>
<body>

<section class="spread spread--outside">
  <article class="panel order">
    <div class="photo order__photo" role="img" aria-label="Photo of smiling school children lying on grass"></div>
    <div class="brand order__brand"><i></i>Lakeside Family</div>
    <div class="form-lines">
      <div>Company Name <span class="line"></span></div>
      <div>Contact Name <span class="line"></span></div>
      <div>Address <span class="line"></span></div>
      <div>Phone <span class="line"></span> Email <span class="line"></span></div>
    </div>
    <table class="levels">
      <tr><td>Exhibitor</td><td>$350</td></tr>
      <tr><td>"Class Sponsor" &amp; Premium Exhibitor</td><td>$750</td></tr>
      <tr><td>Back to School Fair "Recess Sponsor"</td><td>$1,500</td></tr>
      <tr><td>Back to School Fair "Straight A's Sponsor"</td><td>$2,500</td></tr>
      <tr><td>Back to School Fair "Favorite Teacher Sponsor"</td><td>$3,500</td></tr>
      <tr><td>Back to School Fair Naming &amp; "Principal Sponsor"</td><td>$5,000</td></tr>
    </table>
    <div class="order__sign">
      <div>Total Amount Due:</div>
      <div>Signature:</div>
      <p class="small" style="margin-top:8px">Please return this form with payment to reserve your space. Spaces are limited and assigned in order received.</p>
    </div>
    <div class="order__band"></div>
  </article>

  <article class="panel cover">
    <div class="photo cover__photo" role="img" aria-label="Photo of a surprised young girl with pigtails"></div>
    <svg class="cover__curve" width="400" height="60" viewBox="0 0 400 60" aria-hidden="true">
      <path d="M0 40 Q200 -10 400 30 L400 60 L0 60Z" fill="var(--paper)"/>
      <path d="M0 40 Q200 -10 400 30" fill="none" stroke="var(--pink)" stroke-width="4"/>
    </svg>
    <div class="badge">Come Aboard<br>Back to School Fair</div>
    <h1 class="serif cover__title">Sponsorship<br>Opportunities &amp; Exhibitor Info</h1>
    <p class="cover__lede">Reach, interact, and showcase services or products to 3,000+ parents and school-age children</p>
    <div class="cover__brand-wrap">Lakeside</div>
    <div class="brand cover__brand"><i></i>Lakeside Family</div>
  </article>
</section>

<section class="spread spread--inside">
  <article class="panel intro">
    <div class="brand intro__brand"><i></i>Lakeside Family</div>
    <p class="small intro__text">Back to School Fair is an annual opportunity for businesses to communicate directly with local families as they prepare for the new school year. Our readers trust us for ideas, resources and events that help their children thrive, and this fair brings that trust to life in one lively afternoon.</p>
    <div class="photo intro__photo" role="img" aria-label="Photo of a child reading a book"></div>
    <div class="datebox">Saturday, August 5, 2017 · 10am–2pm<br>Riverside Commons<br>Center Court &amp; Lower Level</div>
    <div class="who">
      <h2 class="h-pink">Who</h2>
      <p class="small">Families with children from preschool through high school attend to shop supplies, meet schools and camps, enjoy activities and collect giveaways. Last year more than 3,000 parents and kids joined us.</p>
    </div>
    <div class="why">
      <h2 class="h-pink">Why Exhibit</h2>
      <p class="small">Meet parents face to face, sample products, collect leads and build lasting goodwill. Every exhibitor receives promotion in print, online and in our weekly newsletter, plus a listing in the event program handed to every guest.</p>
    </div>
    <svg class="intro__curve" width="400" height="24" viewBox="0 0 400 24" aria-hidden="true"><path d="M0 24 Q200 -8 400 16 L400 24Z" fill="var(--pink)"/></svg>
    <div class="intro__band">To reserve Back to School Fair space, contact us at 555-012-3456<br>or email info@lakesidefamily.example</div>
  </article>

  <article class="panel tiers">
    <div class="photo tiers__photo" role="img" aria-label="Photo of school children raising hands in class"></div>
    <div class="tier small" style="left:24px;top:142px">
      <h2 class="h-pink">Back to School Fair "Principal Sponsor" $5,000</h2>
      <ul>
        <li>Naming rights on event and all signage</li>
        <li>Premium booth location, double space</li>
        <li>Full page ad in two magazine issues</li>
        <li>Logo on all print and digital promotion</li>
        <li>Dedicated email to subscribers</li>
        <li>Stage mention throughout the day</li>
      </ul>
    </div>
    <div class="tier small" style="left:206px;top:142px">
      <h2 class="h-pink">Back to School Fair "Recess Sponsor" $1,500</h2>
      <ul>
        <li>Sponsor of the kids activity zone</li>
        <li>Booth space with table and chairs</li>
        <li>Half page ad in one magazine issue</li>
        <li>Name on event web page</li>
      </ul>
    </div>
    <div class="tier small" style="left:24px;top:252px">
      <h2 class="h-pink">"Favorite Teacher" $3,500</h2>
      <ul>
        <li>Preferred booth location</li>
        <li>Full page ad in one issue</li>
        <li>Logo on event signage and program</li>
      </ul>
    </div>
    <div class="tier small" style="left:206px;top:252px">
      <h2 class="h-pink">"Class Sponsor" &amp; Premium Exhibitor $750</h2>
      <ul>
        <li>Booth in high traffic area</li>
        <li>Quarter page ad in program</li>
        <li>Social media mention</li>
      </ul>
    </div>
    <div class="photo tiers__inset" role="img" aria-label="Photo of two kids smiling with backpacks"></div>
    <div class="tier small" style="left:206px;top:338px">
      <h2 class="h-pink">"Straight A's Sponsor" $2,500</h2>
      <ul>
        <li>Booth space near main entrance</li>
        <li>Half page ad in two issues</li>
        <li>Logo on event web page</li>
      </ul>
      <h2 class="h-pink" style="margin-top:8px">Exhibitor $350</h2>
      <ul>
        <li>Booth space, table and two chairs</li>
        <li>Listing in the event program</li>
      </ul>
    </div>
    <svg class="tiers__curve" width="400" height="48" viewBox="0 0 400 48" aria-hidden="true"><path d="M0 30 Q200 0 400 24 L400 48 L0 48Z" fill="var(--pink)"/></svg>
  </article>
</section>

</body>
</html>
```